I need a letterhead for a newsletter that will go out quarterly to the dentists of the 18th district. It is called "The Quarterly Ledger" We are in Amarillo TX and have this landmark in the photo as our most prominent feature. If it could be used, that would be cool.
This is a professional organization newsletter so the letterhead should be somewhat professional.

Target Market(s)

Dentists

Industry/Entity Type

Dental

Font styles to use
Serif

Colors

Designer to choose only greyscale colors for use in the design.

Requirements
Must have
• I want the title of "The Quarterly Ledger" to be the on top with the phrase "Brookvale Regional Dental Guild" written underneath.
Nice to have
• the photo incorporated could be incorporated in black and white or color along the bottom of the letterhead or with the title inside the photo.
Should not have
• I don't want it to be cartoony. I want it to be stylish and elegant and professional.

```html
<!DOCTYPE html>
<html lang="en">
<head>
<meta charset="utf-8">
<title>The Quarterly Ledger — Letterhead</title>
<link rel="stylesheet" href="https://fonts.googleapis.com/css2?family=EB+Garamond:wght@400;700&family=Open+Sans:wght@400;700&family=Great+Vibes&display=swap">
<style>
  :root {
    --backdrop: #ecebe8;
    --paper: #ffffff;
    --ink: #111111;
    --ink-soft: #2b2b2b;
    --subtitle-grey: #7a7a7a;
    --rule: #333333;
    --footer-text: #555555;
    --footer-band: #5f5f5f;
  }
  * { margin: 0; padding: 0; box-sizing: border-box; }
  html, body {
    width: 1200px;
    height: 800px;
    overflow: hidden;
    background: var(--backdrop);
  }
  .canvas {
    width: 1200px;
    height: 800px;
    display: flex;
    align-items: center;
    justify-content: center;
  }
  .letterhead {
    position: relative;
    width: 540px;
    height: 764px;
    background: var(--paper);
    box-shadow: 0 2px 10px rgba(0,0,0,0.08);
    overflow: hidden;
  }
  .masthead {
    position: absolute;
    left: 52px;
    top: 58px;
    right: 52px;
  }
  .masthead__title {
    font-family: "EB Garamond", Georgia, serif;
    font-weight: 700;
    font-size: 29px;
    letter-spacing: 0.2px;
    color: var(--ink);
    line-height: 1;
    text-transform: uppercase;
  }
  .masthead__subtitle-row {
    display: flex;
    align-items: flex-end;
    gap: 8px;
    margin-top: 3px;
  }
  .masthead__subtitle {
    font-family: "EB Garamond", Georgia, serif;
    font-size: 15px;
    color: var(--subtitle-grey);
    white-space: nowrap;
    line-height: 1.1;
  }
  .masthead__rule {
    flex: 1;
    height: 1.5px;
    background: var(--rule);
    margin-bottom: 3px;
  }
  .letter-date {
    position: absolute;
    right: 72px;
    top: 222px;
    font-family: "Open Sans", Arial, sans-serif;
    font-size: 9px;
    color: var(--ink);
  }
  .letter-body {
    position: absolute;
    left: 90px;
    right: 72px;
    top: 280px;
    font-family: "Open Sans", Arial, sans-serif;
    font-size: 8.6px;
    line-height: 13.5px;
    color: var(--ink-soft);
  }
  .letter-body p { margin-bottom: 12px; }
  .sign-off {
    position: absolute;
    right: 90px;
    top: 600px;
    text-align: left;
  }
  .sign-off__signature {
    font-family: "Great Vibes", cursive;
    font-size: 24px;
    color: var(--ink);
    line-height: 1;
    margin-left: -24px;
  }
  .sign-off__name {
    font-family: "Open Sans", Arial, sans-serif;
    font-weight: 700;
    font-size: 8.6px;
    color: var(--ink);
    margin-top: 6px;
  }
  .sign-off__role {
    font-family: "Open Sans", Arial, sans-serif;
    font-size: 8.6px;
    color: var(--ink);
    line-height: 1.1;
  }
  .contact-footer {
    position: absolute;
    left: 52px;
    right: 52px;
    bottom: 38px;
    font-family: "EB Garamond", Georgia, serif;
    color: var(--footer-text);
  }
  .contact-footer__web {
    font-size: 10.5px;
    letter-spacing: 2px;
    margin-bottom: 6px;
  }
  .contact-footer__details {
    display: flex;
    gap: 14px;
    font-size: 8.6px;
  }
  .contact-footer__label { margin-right: 4px; }
  .footer-band {
    position: absolute;
    left: 0;
    right: 0;
    bottom: 0;
    height: 18px;
    background: var(--footer-band);
  }
</style>
</head>
<body>
<main class="canvas">
  <article class="letterhead">
    <header class="masthead">
      <h1 class="masthead__title">The Quarterly Ledger</h1>
      <div class="masthead__subtitle-row">
        <span class="masthead__subtitle">Brookvale Regional Dental Guild</span>
        <span class="masthead__rule"></span>
      </div>
    </header>

    <p class="letter-date">Date, 10 September, 2019</p>

    <section class="letter-body">
      <p>This is a sample letter that has been placed to demonstrate typing remat (Your Company). letterhead design. When positioned properly, it will serve to work in harmony with all other elements letterhead. This letterhead design is meant to project an image</p>
      <p>This letterhead design is meant project an image of professionalism reliability. By using simple aligen we have created a very spacious feeling. The simplicity suggest rengththe spaciousnes contributes h aesthetics the layout. These basic qualities along with the (Your Company)</p>
      <p>look and helps reinforce the (Your Company) brand. letterhead design is meant to project an image p design. When positioned properly, it will serve to work in harmony all the other elements letterhead. sionalism and reliability.</p>
      <p>This letterhead design is based on the (Form of your logo) form (Your Company) logo. Each stationery we have created a very spacious feeling. The simplicity suggests strength the spaciousnes contribute part of the (Form of your logo).</p>
    </section>

    <div class="sign-off">
      <div class="sign-off__signature">Daniel Harrow</div>
      <div class="sign-off__name">Daniel Harrow</div>
      <div class="sign-off__role">Manager</div>
    </div>

    <footer class="contact-footer">
      <div class="contact-footer__web">www.brookvaleguild.org</div>
      <div class="contact-footer__details">
        <span><span class="contact-footer__label">A :</span>418 Cedar Row, Suite 210</span>
        <span><span class="contact-footer__label">E:</span>info@brookvaleguild.org</span>
        <span><span class="contact-footer__label">P:</span>555-014-2290</span>
      </div>
    </footer>
    <div class="footer-band"></div>
  </article>
</main>
</body>
</html>
```